wordpress website Clara Whitby, Author, Speaker and Coach

Need a wordpress blogging website for author/speaker/coach.
I have paid for hosting on bytebarn.
I am currently writing a book - Launchpad to Campus - Steps and strategies to prepare you to thrive in college and beyond. Eventually, I will have an Academic/Life Coaching program targeting high school and college students. This website's purpose is to build my email list. I can offer the following reports as incentive for email sign-up:
1. Seven Habits That Get Your Teen Through University on Schedule and on Budget
2. Clever Routes to Fund Tuition Costs
3. QRE/BTX vocabulary word of the day

facebook page: https://www.facebook.com/Clara-Whitby-AcademicLife-Coach-839205517364028/

I would like to have these pages:

1. Home or About page

High school is becoming more and more stressful for students. Not only are they taking more ZL classes than ever before, and often spending $1,000’s on QRE/BTX prep programs, most are NOT prepared for success in college. Only 19% of students are graduating from college within 4 years and only 56% are graduating within 6 years. With the cost of higher education skyrocketing, each extra year of school can costs families $40,000 - $60,000 when you factor in living expenses. Then, when students do graduate, they are often underemployed.

Clara's approach is whole person oriented. Her programs help students learn life skills in addition to the study, time management skills, etc. offered by most academic coaching programs. Our program addresses all of the major causes of failure to graduate within 4 years, and is based on sound educational research. Clara's program initially provides the daily interaction needed to successfully change behaviors and seat new success habits, unlike many programs in which students interact with coaches only once a week.
Bio
Clara Whitby is a certified teacher and holds advanced certification in academic coaching and tutoring. She also is a certified trainer in the Miles Ferrow Growth Pathways. She has three successful adult children, and helped them overcome learning differences and thrive.

2. Blog

3. Contact - Include form (I split time between USA and Saudi Arabia, so I will call or email people back, but don't want to leave a phone number)
info@clarawhitby.example

4. Store – 1 book for now
Launchpad to Campus
Steps and strategies to prepare you to thrive in college and beyond
Available 12/01/2017
I could make a preview chapter available for download

5. Speaking
Clara Whitby is available for keynote addresses and half-day, full day or multi-day workshops. I will develop details later

6.Coaching programs
I will develop details later

Target Market(s)

high school students who are college bound and their parents

Number of Pages Required

5+ page

Font styles to use
Sans Serif

Colors

Designer to choose colors to be used in the design.

Requirements
Nice to have
• integration with post finch for contact management

```html
<!DOCTYPE html>
<html lang="en">
<head>
<meta charset="utf-8">
<title>Clara Whitby – Academic/Life Coach</title>
<link href="https://fonts.googleapis.com/css2?family=PT+Sans:ital,wght@0,400;0,700;1,400&family=PT+Serif:ital,wght@0,400;0,700;1,400&display=swap" rel="stylesheet">
<style>
:root{
  --ink:#333333;
  --muted:#777777;
  --line:#e2e2e2;
  --purple:#8a8ccc;
  --purple-dark:#7577c0;
  --green:#8dc63f;
  --band:#ebebed;
  --footer:#161616;
  --footer-bottom:#0b0b0b;
  --white:#ffffff;
}
*{margin:0;padding:0;box-sizing:border-box}
html,body{width:1200px;height:2326px;overflow:hidden;background:var(--white)}
body{position:relative;font-family:"PT Sans",Arial,sans-serif;color:var(--ink)}
.abs{position:absolute}
.icon-dot{display:inline-block;width:9px;height:9px;border-radius:50%;background:#444}
/* header */
.site-header .social{left:24px;top:44px;display:flex;gap:19px}
.brand{left:0;width:1200px;top:40px;display:flex;flex-direction:column;align-items:center;gap:8px}
.brand-mark{width:34px;height:34px;border-radius:50%;background:var(--green)}
.brand-name{font-family:"PT Sans",sans-serif;font-size:13px;color:var(--green);font-weight:700}
.tools{right:24px;top:40px;display:flex;gap:26px;align-items:center}
.rule{left:24px;width:1152px;height:1px;background:var(--line)}
.main-nav{left:0;width:1200px;top:137px;display:flex;justify-content:center;font-size:10.5px;letter-spacing:.5px;text-transform:uppercase;color:#666}
.main-nav a{padding:0 20px;border-left:1px solid #bbb;line-height:13px;color:inherit;text-decoration:none}
.main-nav a:first-child{border-left:none;color:var(--purple)}
/* hero */
.hero{left:24px;top:197px;width:1152px;height:450px;display:flex;gap:6px}
.hero-card{position:relative;flex:1}
.hero-photo{position:absolute;inset:0}
.hero-caption{position:absolute;left:0;right:0;top:291px;height:99px;color:var(--white);text-align:center;padding-top:18px}
.hero-caption h2{font-family:"PT Serif",serif;font-weight:700;font-size:15.5px;line-height:20px}
.hero-caption span{display:block;margin-top:10px;font-size:10px;font-weight:700}
.cap-purple{background:rgba(138,140,204,.93)}
.cap-green{background:rgba(141,198,63,.95)}
/* welcome */
.welcome{left:24px;top:680px;width:1152px;height:387px;background:var(--band)}
.welcome-photo{left:148px;top:75px;width:270px;height:237px}
.welcome h1{left:444px;top:68px;font-family:"PT Serif",serif;font-weight:400;font-size:23px;color:#444}
.welcome p{left:444px;top:128px;width:576px;font-size:11px;line-height:21px;color:var(--muted)}
.welcome .social{left:444px;top:278px;display:flex;gap:19px}
.badge{left:898px;top:272px;width:96px;height:96px;border-radius:50%;background:radial-gradient(circle,#e6e6e6,#b4b4b4);border:3px solid #d0d0d0}
/* posts */
.section-title{left:187px;top:1109px;font-family:"PT Serif",serif;font-size:22px;color:#444}
.post{left:172px;width:562px;height:213px;border:1px solid var(--line);background:var(--white)}
.post-img{position:absolute;top:-1px;width:270px;height:213px}
.post-body{position:absolute;top:0;width:270px;padding:18px 19px}
.post-body h3{font-family:"PT Serif",serif;font-weight:700;font-size:15px;line-height:20px;color:#333}
.post-body p{margin-top:16px;font-size:11px;line-height:20px;color:var(--muted)}
.post-meta{display:flex;justify-content:space-between;align-items:center;margin-top:14px;font-size:10px;color:var(--purple);font-weight:700}
.post-meta .share{display:flex;gap:12px}
.post-meta .icon-dot{width:7px;height:7px}
/* sidebar */
.newsletter{left:758px;top:1115px;width:268px;height:343px;background:var(--green);color:var(--white);padding:18px 14px}
.newsletter h2{font-family:"PT Serif",serif;font-weight:400;font-size:21px;padding-bottom:10px;border-bottom:1px solid rgba(255,255,255,.7)}
.newsletter p{margin-top:16px;font-size:10.5px;line-height:17px}
.newsletter ul{margin-top:16px;padding-left:14px;font-size:10.5px;line-height:14px}
.newsletter li{margin-bottom:14px}
.newsletter .field{margin-top:16px;height:34px;background:#f3f3f3;color:#999;font-style:italic;font-size:11px;padding:10px 10px;margin-left:4px;width:230px}
.newsletter .submit{margin-top:8px;height:34px;background:var(--purple);font-size:14px;font-weight:700;text-align:center;line-height:34px;margin-left:4px;width:230px}
.quote-box{left:758px;top:1481px;width:268px;height:271px;background:#efeff0;border:1px solid #ddd}
.quote-nav{right:0;top:0;display:flex}
.quote-nav span{width:22px;height:22px;border:1px solid #ccc;background:var(--white);font-size:12px;line-height:20px;text-align:center}
.quote-avatar{left:82px;top:31px;width:104px;height:104px;border-radius:50%;border:4px solid var(--white);background:linear-gradient(#6a5a52,#2a2222)}
.quote-mark{left:10px;top:118px;font-family:"PT Serif",serif;font-size:110px;color:#dadadc;line-height:1}
.quote-text{left:14px;width:240px;top:161px;text-align:center;font-family:"PT Serif",serif;font-style:italic;font-size:12px;line-height:20px;color:#555}
.quote-label{left:0;width:268px;top:228px;text-align:center;font-family:"PT Serif",serif;font-size:14px;color:var(--purple)}
/* pagination */
.pager{left:414px;top:1917px;display:flex;gap:8px}
.pager span{width:17px;height:17px;border:1px solid #ccc;font-size:9px;text-align:center;line-height:15px}
.pager-next{left:643px;top:1919px;font-size:12px;color:#555}
/* footer */
.site-footer{left:0;top:1974px;width:1200px;height:306px;background:var(--footer);color:var(--white)}
.footer-brand{left:205px;top:42px;display:flex;flex-direction:column;align-items:center;gap:8px}
.footer-brand .brand-mark{background:var(--white);width:30px;height:30px}
.footer-brand .brand-name{color:var(--white)}
.footer-about{left:193px;top:128px;width:226px;font-size:11px;line-height:17px;font-style:italic;color:#ddd}
.footer-social{left:236px;top:256px;display:flex;gap:14px}
.footer-social span{width:22px;height:22px;border-radius:50%;background:#3a3a3a}
.footer-latest h4{position:absolute;left:477px;top:56px;font-family:"PT Serif",serif;font-weight:400;font-size:15px;letter-spacing:.5px}
.latest-item{left:465px;width:272px;display:flex;gap:13px;font-size:11px;line-height:17px;color:#ddd}
.latest-item .thumb{flex:none;width:44px;height:44px;border-radius:50%;background:linear-gradient(#cfc7c2,#9a8f8a)}
.latest-item small{display:block;margin-top:6px;font-size:11px}
.latest-sep{left:465px;top:148px;width:272px;height:1px;background:#333}
.fb-box{left:772px;top:75px;width:240px;height:171px;background:var(--white);color:#333;font-size:9px;padding:8px}
.fb-cover{height:88px;background:linear-gradient(#f1f1f1,#d9d9d9);position:relative}
.fb-cover b{position:absolute;left:60px;top:8px;font-size:9px}
.fb-buttons{display:flex;justify-content:space-between;margin-top:6px}
.fb-buttons span{border:1px solid #ccc;padding:1px 5px;font-weight:700}
.fb-box p{margin-top:8px}
.fb-faces{display:flex;gap:4px;margin-top:6px}
.fb-faces span{width:15px;height:15px;background:#b9aca4}
.to-top{left:1043px;top:2250px;width:40px;height:32px;background:var(--green)}
.footer-bottom{left:0;top:2280px;width:1200px;height:46px;background:var(--footer-bottom);color:#bbb;font-size:11px;padding:17px 0 0 179px}
</style>
</head>
<body>

<header class="site-header">
  <div class="abs social" aria-label="Social links"><span class="icon-dot"></span><span class="icon-dot"></span><span class="icon-dot"></span><span class="icon-dot"></span></div>
  <div class="abs brand"><span class="brand-mark"></span><span class="brand-name">Upward Bloom Coaching</span></div>
  <div class="abs tools">
    <svg width="16" height="16" viewBox="0 0 16 16" aria-label="Search"><circle cx="6.5" cy="6.5" r="5" fill="none" stroke="#333" stroke-width="2"/><line x1="10.3" y1="10.3" x2="15" y2="15" stroke="#333" stroke-width="2.2"/></svg>
    <svg width="14" height="12" viewBox="0 0 14 12" aria-label="Menu"><rect y="0" width="14" height="2" fill="#333"/><rect y="5" width="14" height="2" fill="#333"/><rect y="10" width="14" height="2" fill="#333"/></svg>
  </div>
  <div class="abs rule" style="top:124px"></div>
  <nav class="abs main-nav"><a href="#">Home</a><a href="#">Blog</a><a href="#">Contact</a><a href="#">Store</a><a href="#">Speaking</a><a href="#">Coaching Programs</a></nav>
  <div class="abs rule" style="top:165px"></div>
</header>

<section class="abs hero">
  <article class="hero-card">
    <div class="hero-photo" role="img" aria-label="Photo of a graduate in cap and gown hugging her mother" style="background:linear-gradient(160deg,#cfd8b4,#6b5d58 55%,#1e1a1a)"></div>
    <div class="hero-caption cap-purple"><h2>Seven Habits That Get Your Teen<br>Through University on Schedule</h2><span>Sign up to know &raquo;</span></div>
  </article>
  <article class="hero-card">
    <div class="hero-photo" role="img" aria-label="Photo of a graduation cap resting on banknotes" style="background:linear-gradient(160deg,#d8dcd4,#a8ada4 60%,#c7cbc4)"></div>
    <div class="hero-caption cap-green"><h2>Clever Routes to Fund<br>Tuition Costs</h2><span>Sign up to know &raquo;</span></div>
  </article>
  <article class="hero-card">
    <div class="hero-photo" role="img" aria-label="Photo of a hand holding a pencil over an open book" style="background:linear-gradient(160deg,#7a5a48,#c9b3a4 50%,#e8e6f0)"></div>
    <div class="hero-caption cap-purple"><h2>Seven Habits That Get Your Teen<br>Through University on Schedule</h2><span>Sign up to know &raquo;</span></div>
  </article>
</section>

<section class="abs welcome">
  <div class="abs welcome-photo" role="img" aria-label="Portrait photo of Clara Whitby" style="background:linear-gradient(150deg,#5a4638,#2b2220 60%,#141010)"></div>
  <h1 class="abs">Welcome To Clara’s Upward Bloom Coaching</h1>
  <p class="abs">Clara Whitby is a certified teacher and holds advanced certification in academic coaching and tutoring. She also is a certified trainer in the Miles Ferrow Growth Pathways. She has 3 successful adult children, and helped them overcome learning differences and thrive. Clara’s approach is whole person oriented. Her programs help students learn life skills in addition to the study, time management skills, etc. offered by most academic coaching programs. Clara’s program provides the daily interaction needed to successfully change behaviors and seat new success habits, unlike programs in which students only interact with coaches once a week.</p>
  <div class="abs social"><span class="icon-dot"></span><span class="icon-dot"></span><span class="icon-dot"></span><span class="icon-dot"></span></div>
  <div class="abs badge" role="img" aria-label="Certified trainer seal"></div>
</section>

<h2 class="abs section-title">Recent Posts</h2>
<div class="abs rule" style="left:172px;width:562px;top:1145px"></div>

<article class="abs post" style="top:1183px">
  <div class="post-img" style="left:-1px;background:linear-gradient(150deg,#e4e8e4,#9fa8a2)" role="img" aria-label="Photo of a pencil on an answer sheet"></div>
  <div class="post-body" style="left:270px">
    <h3>Lorem ipsum dolor sit amet, consectetuer adipis</h3>
    <p>Ut wisi enim ad minim veniam, quis nostrud exerci tation ullamcorper suscipit lobortis nisl ut aliquip ex ea commodo consequat. Duis autem vel eum iriure dolor in hendrerit</p>
    <div class="post-meta"><span>Continue reading &raquo;</span><span class="share"><span class="icon-dot"></span><span class="icon-dot"></span><span class="icon-dot"></span></span></div>
  </div>
</article>

<article class="abs post" style="top:1418px">
  <div class="post-body" style="left:0">
    <h3>Lorem ipsum dolor sit amet, consectetuer adipis</h3>
    <p>Ut wisi enim ad minim veniam, quis nostrud exerci tation ullamcorper suscipit lobortis nisl ut aliquip ex ea commodo consequat. Duis autem vel eum iriure dolor in hendrerit</p>
    <div class="post-meta"><span>Continue reading &raquo;</span><span class="share"><span class="icon-dot"></span><span class="icon-dot"></span><span class="icon-dot"></span></span></div>
  </div>
  <div class="post-img" style="right:-1px;background:linear-gradient(150deg,#5a3a26,#2a1a12)" role="img" aria-label="Photo of a savings jar with coins and a tag"></div>
</article>

<article class="abs post" style="top:1656px">
  <div class="post-img" style="left:-1px;background:linear-gradient(150deg,#dfe2da,#5b4d44 55%,#8a6a3a)" role="img" aria-label="Photo of a graduate at a ceremony"></div>
  <div class="post-body" style="left:270px">
    <h3>Lorem ipsum dolor sit amet, consectetuer adipis</h3>
    <p>Ut wisi enim ad minim veniam, quis nostrud exerci tation ullamcorper suscipit lobortis nisl ut aliquip ex ea commodo consequat. Duis autem vel eum iriure dolor in hendrerit</p>
    <div class="post-meta"><span>Continue reading &raquo;</span><span class="share"><span class="icon-dot"></span><span class="icon-dot"></span><span class="icon-dot"></span></span></div>
  </div>
</article>

<aside class="abs newsletter">
  <h2>Newsletter</h2>
  <p>Join our newsletter &amp; get latest updates on I can offer the following reports:</p>
  <ul>
    <li>Seven Habits That Get Your Teen Through University on Schedule and on Budget</li>
    <li>Clever Routes to Fund Tuition Costs</li>
    <li>QRE/BTX vocabulary word of the day</li>
  </ul>
  <div class="field">Your mail id...</div>
  <div class="submit">Submit</div>
</aside>

<aside class="abs quote-box">
  <div class="abs quote-nav"><span>&lsaquo;</span><span>&rsaquo;</span></div>
  <div class="abs quote-avatar" role="img" aria-label="Portrait of Clara Whitby"></div>
  <div class="abs quote-mark">&ldquo;</div>
  <p class="abs quote-text">“Sa non numquam eius modi temp ora incidunt ut labore et dolore magnam aliquam quaerat.”</p>
  <div class="abs quote-label">Quote of the Day</div>
</aside>

<div class="abs pager"><span>1</span><span>2</span></div>
<div class="abs pager-next">Next &raquo;</div>

<footer class="abs site-footer">
  <div class="abs footer-brand"><span class="brand-mark"></span><span class="brand-name">Upward Bloom Coaching</span></div>
  <p class="abs footer-about">Sed ut perspiciatis unde omnis iste natus error sit voluptatem accusan tium doloremque laudantium, totam rem aperiam, eaque ipsa quae ab illo inve ntore veritatis et quasi arch.</p>
  <div class="abs footer-social"><span></span><span></span><span></span><span></span><span></span></div>
  <div class="footer-latest"><h4>Latest Posts</h4></div>
  <div class="abs latest-item" style="top:90px"><span class="thumb" role="img" aria-label="Post thumbnail"></span><div>Quis nostrum exercitationem ullam corporis suscipit.<small>October 10, 2015</small></div></div>
  <div class="abs latest-sep"></div>
  <div class="abs latest-item" style="top:168px"><span class="thumb" role="img" aria-label="Post thumbnail"></span><div>Et harum quidem rerum facil es est et expedita distinctio. Nam<small>October 08, 2015</small></div></div>
  <div class="abs fb-box">
    <div class="fb-cover" role="img" aria-label="Social page cover"><b>Clara Whitby - Academic/Life Coach</b></div>
    <div class="fb-buttons"><span>Like Page</span><span>Share</span></div>
    <p>Be the first of your friend to like this</p>
    <div class="fb-faces"><span></span><span></span><span></span><span></span><span></span><span></span><span></span></div>
  </div>
</footer>
<a class="abs to-top" aria-label="Back to top"><svg width="40" height="32" viewBox="0 0 40 32"><polyline points="15,18 20,13 25,18" fill="none" stroke="#fff" stroke-width="2"/></svg></a>
<div class="abs footer-bottom">Copyright © Clara Whitby - Academic/Life Coach 2017</div>

</body>
</html>
```